Tattoo Removal Company Needs A New Business Card

We need a business card design for a new tattoo removal company based out of Phoenix Arizona. This company has a new hipster style website using tones of gray with a pop of teal. I have attached two images of their homepage and also their logo. This card should have feel of website but be equally functional.

Target Market(s)

women and men looking to have tattoos removed 20's to 40's

Industry/Entity Type

Business

Contact Information for Business Card

Marta Denby, Office Manager
Address: 7315 W Copper Basin Ave STE 406
Phone: 602-555-3917

Colors
00a990
0592cd

Requirements
Must have
• Must have a similar feel and tone as website.

```html
<!DOCTYPE html>
<html lang="en">
<head>
<meta charset="utf-8">
<title>Saguaro Tattoo Removal – Business Card</title>
<link rel="stylesheet" href="https://fonts.googleapis.com/css2?family=Kreon:wght@400;700&family=Crimson+Text:wght@400&family=Tinos:wght@400;700&display=swap">
<style>
  :root {
    --backdrop: #e9e6e1;
    --card-white: #ffffff;
    --card-grey-light: #b9b9b9;
    --card-grey-mid: #9c9c9c;
    --card-grey-dark: #7d7d7d;
    --photo-dark: #2a2a2a;
    --photo-mid: #6e6e6e;
    --ink: #1e1e1e;
    --ink-soft: #444444;
    --shadow: rgba(0, 0, 0, 0.35);
  }
  * { margin: 0; padding: 0; box-sizing: border-box; }
  html, body {
    width: 1000px;
    height: 1200px;
    overflow: hidden;
    background: var(--backdrop);
  }
  .canvas {
    position: relative;
    width: 1000px;
    height: 1200px;
  }
  .card {
    position: absolute;
    box-shadow: 0 4px 10px var(--shadow);
    overflow: hidden;
  }

  /* Front */
  .card-front {
    left: 78px;
    top: 108px;
    width: 840px;
    height: 492px;
    background: radial-gradient(ellipse at 45% 45%, var(--card-grey-light) 0%, var(--card-grey-mid) 60%, var(--card-grey-dark) 100%);
  }
  .portrait {
    position: absolute;
    right: 0;
    top: 0;
    width: 340px;
    height: 492px;
    background: linear-gradient(100deg, rgba(110,110,110,0) 0%, var(--photo-mid) 35%, var(--photo-dark) 70%, var(--photo-mid) 100%);
  }
  .brand {
    position: absolute;
    font-family: "Kreon", serif;
    font-weight: 700;
    color: var(--ink);
    text-align: center;
    line-height: 1;
  }
  .brand-name {
    display: block;
    font-size: 58px;
    letter-spacing: 2px;
  }
  .brand-tag {
    display: block;
    font-size: 27px;
    letter-spacing: 3px;
    margin-top: 10px;
  }
  .card-front .brand {
    left: 58px;
    top: 62px;
    width: 330px;
  }
  .contact {
    position: absolute;
    left: 59px;
    top: 296px;
    color: var(--ink);
  }
  .contact-name {
    font-family: "Kreon", serif;
    font-weight: 400;
    font-size: 43px;
    line-height: 1;
  }
  .contact-role {
    font-family: "Crimson Text", serif;
    font-size: 21px;
    margin-top: 8px;
  }
  .contact-lines {
    font-family: "Crimson Text", serif;
    font-size: 22px;
    line-height: 31px;
    margin-top: 16px;
  }

  /* Back */
  .card-back {
    left: 78px;
    top: 662px;
    width: 843px;
    height: 494px;
    background: var(--card-white);
  }
  .card-back .brand {
    left: 0;
    right: 0;
    top: 86px;
  }
  .card-back .brand-name { font-size: 64px; }
  .card-back .brand-tag { font-size: 30px; }
  .services {
    position: absolute;
    left: 52px;
    width: 740px;
    top: 296px;
    font-family: "Tinos", serif;
    color: var(--ink);
  }
  .services-title {
    text-align: center;
    font-weight: 700;
    font-size: 22px;
    color: var(--ink-soft);
    letter-spacing: 0.5px;
  }
  .services-text {
    font-size: 18.5px;
    line-height: 28px;
    text-align: justify;
    text-align-last: center;
    margin-top: 6px;
  }
</style>
</head>
<body>
<main class="canvas">

  <section class="card card-front" aria-label="Business card front">
    <div class="portrait" role="img" aria-label="Black and white portrait photograph of a bearded man in a t-shirt, seen in profile"></div>
    <div class="brand">
      <span class="brand-name">SAGUARO</span>
      <span class="brand-tag">TATTOO REMOVAL</span>
    </div>
    <div class="contact">
      <h1 class="contact-name">Marta Denby</h1>
      <p class="contact-role">Office Manager</p>
      <p class="contact-lines">7315 W Copper Basin Ave STE 406<br>Phone: 602-555-3917</p>
    </div>
  </section>

  <section class="card card-back" aria-label="Business card back">
    <div class="brand">
      <span class="brand-name">SAGUARO</span>
      <span class="brand-tag">TATTOO REMOVAL</span>
    </div>
    <div class="services">
      <h2 class="services-title">SERVICES</h2>
      <p class="services-text">ClearWave is a quick and easy non-surgical,non-invesive laser skin treatment for those seeking tattoo removal and skin rejuvenating treatments. Erase unwanted tattoos,pigment,as well as wrinkles and acne sears with the most advenced laser treatment available for safe and effective treatment.</p>
    </div>
  </section>

</main>
</body>
</html>
```